VFX Company Business Card Design Project

The Ember Vale is a decentralized Visual Effects Studio servicing the television and feature film industries.
Project Brief:
Take our logo that was previously designed on Pixel Harbor and make a double sided business card.
Requirements:
- Card MUST be double sided.
- Front of card MUST have the yellow part of our logo against the dark grey background.
- Back of card is completely up to the designer.
- Back of card must include the complete company logo.
Please follow these File Preparation guidelines:
http://printmoor.example/infopage?file=filetype_en&s=PrintMoor_new&lang=en
Industry/Entity Type
Business
Look and feel
Each slider illustrates characteristics of the customer's brand and the style your logo design should communicate.

```html
<!DOCTYPE html>
<html lang="en">
<head>
<meta charset="utf-8">
<title>The Ember Vale – Business Card</title>
<link rel="stylesheet" href="https://fonts.googleapis.com/css2?family=Questrial&display=swap">
<style>
  :root {
    --page: #ffffff;
    --card-dark: #262626;
    --card-light: #ffffff;
    --accent: #f2b91c;
    --accent-soft: #f4c73a;
    --ink: #1c1c1c;
    --ink-mid: #555555;
    --ink-grey: #7a7a7a;
    --rule: #bdbdbd;
  }
  * { margin: 0; padding: 0; box-sizing: border-box; }
  html, body {
    width: 936px; height: 1200px; overflow: hidden;
    background: var(--page);
    font-family: "Questrial", "Century Gothic", sans-serif;
  }
  .canvas { position: relative; width: 936px; height: 1200px; }

  .card { position: absolute; left: 66px; width: 806px; }

  /* Front side */
  .card--front {
    top: 53px; height: 521px;
    background: var(--card-dark);
    display: flex; align-items: center; justify-content: center;
  }
  .brand { display: flex; align-items: center; gap: 20px; }
  .brand__dot {
    width: 46px; height: 46px; border-radius: 50%;
    background: var(--accent);
  }
  .brand__name {
    font-size: 56px; color: var(--accent); letter-spacing: 1px;
    white-space: nowrap;
  }

  /* Back side */
  .card--back {
    top: 634px; height: 502px;
    background: var(--card-light);
  }
  .brand--small { position: absolute; left: 29px; top: 24px; gap: 10px; }
  .brand--small .brand__dot { width: 20px; height: 20px; }
  .brand--small .brand__name { font-size: 24px; }

  .contact { position: absolute; right: 17px; text-align: right; white-space: nowrap; }
  .person { top: 136px; font-size: 57px; line-height: 1; color: var(--ink-mid); }
  .person__surname { color: var(--ink); }
  .role { top: 204px; font-size: 34px; line-height: 1; color: var(--accent-soft); }
  .details { top: 290px; font-size: 31px; line-height: 38px; color: var(--ink); }
  .details__label { color: var(--accent-soft); }
  .web { top: 462px; font-size: 31px; line-height: 1; color: var(--ink-grey); }

  .trim-mark {
    position: absolute; left: 66px; top: 1136px;
    width: 59px; height: 2px; background: var(--rule);
  }
</style>
</head>
<body>
<main class="canvas">
  <section class="card card--front" aria-label="Card front">
    <div class="brand">
      <span class="brand__dot"></span>
      <span class="brand__name">The Ember Vale</span>
    </div>
  </section>

  <section class="card card--back" aria-label="Card back">
    <div class="brand brand--small">
      <span class="brand__dot"></span>
      <span class="brand__name">The Ember Vale</span>
    </div>

    <p class="contact person">Nora <span class="person__surname">Fieldhouse</span></p>
    <p class="contact role">Graphic Designer</p>
    <p class="contact details">
      <span class="details__label">T:</span> 01632 960418<br>
      <span class="details__label">M:</span> 07700 900234<br>
      <span class="details__label">E:</span> hello@embervale.example
    </p>
    <p class="contact web">www.embervale.example</p>
  </section>

  <div class="trim-mark"></div>
</main>
</body>
</html>
```